Rent a Velvet needs a Stunning web design

Rent a Velvet is an upmarket agency in Sydney that has lingerie waitresses for events.

Rent a Velvet is looking for a website design that is as sexy and sophisticated as the ladies who work for them!

The design mustn't be cluttered, tacky or pornographic. What I'm looking for is something better than the industry leader www.glimmerdolls.com.au Something classy, sexy and different.

When designing please suggest a CMS, we already use wordpress but are open to suggestions.

We will need a home page that incorporates a feed from a blog and/or social media (please make suggestions and use your discretion as a designer, however we'd like to approve what goes into the feed before it goes in.) The home page could also have a list of our services, but if not we will need a services page. Our Services include:
Lingerie waitressing at events
Lingerie waitresses to help dress the groom pre wedding.
Bucks parties

We have a logo that we'd like incorporated into the design and have attached it.

We will also need a portfolio page for the ladies, This is not to be cluttered, tacky or pornographic. It needs to be classy.

We will also need a "Contact us" page and were thinking that this could potentially also be a "Ask for a quote on your event" page. I.e. have a regular "Contact us" form but have alternate fields if they tick the "I want a quote" box. Alternatively you could have two parts to the contact us page. One that is a regular form and one that has a "Your requirements" box.

Again please use your discretion when designing these, if it's too cluttered it won't work. If it looks tacky, don't do it. If you have suggestions make them.

Target Market(s)

Males between the ages of 18 - 45

Industry/Entity Type

Industry

Requirements
Must have
• Must incorporate our logo.

```html
<!DOCTYPE html>
<html lang="en">
<head>
<meta charset="utf-8">
<title>Rent a Velvet</title>
<link href="https://fonts.googleapis.com/css2?family=Roboto:wght@400;500;700&family=Roboto+Condensed:wght@400;700&display=swap" rel="stylesheet">
<style>
:root{
  --red:#e0193a;
  --ink:#111;
  --grey:#777;
  --line:#cfcfcf;
  --footer:#2b2b2b;
  --bg:#fff;
  --skin-a:#e9c7ab;
  --skin-b:#c9977a;
}
*{box-sizing:border-box;margin:0;padding:0}
html,body{width:889px;height:1200px;overflow:hidden;background:var(--bg)}
body{font-family:"Roboto",Arial,sans-serif;color:var(--ink)}
.page{position:relative;width:1020px;height:1377px;transform:scale(.8716);transform-origin:0 0}
.abs{position:absolute}
.header{left:40px;top:6px;width:940px;height:150px;border:1px solid var(--line)}
.brand{left:63px;top:58px;display:flex;align-items:center;gap:12px;color:var(--red);font-family:"Roboto Condensed",sans-serif;font-weight:700;font-size:38px}
.brand-dot{width:18px;height:18px;border-radius:50%;background:var(--red)}
.account{left:567px;top:34px;display:flex;align-items:center;gap:10px;font-size:12px;color:var(--grey)}
.account .sep{color:var(--line)}
.social{left:800px;top:30px;display:flex;gap:6px}
.social span{width:25px;height:25px;background:#bcd3e8;border:1px solid #9fb6cc;border-radius:3px}
.search{left:625px;top:94px;display:flex;gap:3px}
.search input{width:180px;height:30px;border:1px solid var(--line);padding:0 14px;font:13px "Roboto",sans-serif;color:#aaa}
.search button{width:51px;height:30px;border:0;background:var(--red);color:#fff;font:700 22px "Roboto Condensed",sans-serif}
.nav{left:104px;top:165px;width:796px;display:flex;justify-content:space-between;font-size:15px;letter-spacing:1px}
.nav a{color:var(--ink);text-decoration:none}
.nav a.active{color:var(--red)}
.hero{left:40px;top:191px;width:940px;height:360px;border:1px solid var(--line)}
.hero-title{left:103px;top:282px;font-weight:700;font-size:40px;line-height:1;letter-spacing:.5px}
.hero-sub{left:103px;top:322px;font-family:"Roboto Condensed",sans-serif;font-weight:700;font-size:58px;color:var(--red);line-height:1}
.hero-text{left:104px;top:390px;width:420px;font-size:15.5px;line-height:21px;color:var(--grey);text-transform:uppercase}
.btn{display:flex;align-items:center;justify-content:center;gap:18px;background:var(--ink);color:#fff;font-weight:700;text-decoration:none}
.hero-btn{left:105px;top:484px;width:220px;height:44px;font-size:20px}
.model{left:680px;top:200px;width:120px;height:412px;border-radius:60px 60px 30px 30px;background:linear-gradient(180deg,#6b4a36 0%,var(--skin-a) 25%,var(--skin-b) 100%)}
.dots{left:461px;top:562px;display:flex;gap:8px}
.dots span{width:18px;height:18px;border-radius:50%;background:radial-gradient(circle at 35% 30%,#fff,#ccc)}
.dots span.on{background:radial-gradient(circle at 35% 30%,#ff5a72,var(--red))}
.rule{left:40px;width:940px;height:1px;background:var(--line)}
.card{top:632px;width:210px;height:380px}
.card+.card{border-left:1px solid var(--line)}
.card-photo{left:25px;top:0;width:160px;height:280px;background:linear-gradient(180deg,#7a523c 0%,var(--skin-a) 20%,var(--skin-b) 100%);border:1px solid var(--line)}
.card-title{left:24px;top:312px;font-family:"Roboto Condensed",sans-serif;font-weight:700;font-size:14px;line-height:18px;color:var(--red);letter-spacing:.5px}
.card-note{left:25px;top:358px;font-size:10px;color:var(--grey)}
.section-title{font-family:"Roboto Condensed",sans-serif;font-size:24px;color:var(--red);letter-spacing:.5px}
.services{left:701px;top:650px}
.service-list{left:720px;top:690px;display:grid;grid-template-columns:137px 137px;row-gap:9px;list-style:none;font-size:13px;color:#333}
.service-list li{display:flex;align-items:center;gap:9px;height:18px}
.service-list li::before{content:"";width:10px;height:10px;border-radius:50%;background:radial-gradient(circle at 35% 30%,#ff7a8c,var(--red))}
.post{top:1058px;width:460px;height:160px}
.post-photo{left:0;top:35px;width:120px;height:120px;border:1px solid var(--line);background:linear-gradient(180deg,#6b4a36 0%,var(--skin-a) 35%,var(--skin-b) 100%)}
.post-head{left:136px;top:36px;font-family:"Roboto Condensed",sans-serif;font-weight:700;font-size:17px;color:#222;letter-spacing:.3px}
.post-text{left:136px;top:64px;width:320px;font-size:11.5px;line-height:19px;color:#333}
.post-btn{left:137px;top:133px;width:110px;height:22px;font-size:10px;gap:10px}
.footer{left:40px;top:1262px;width:940px;height:95px;background:var(--footer);color:#eee;font-size:11.5px}
.footer-text{left:23px;top:16px;width:650px;line-height:16px}
.footer-links{left:23px;top:58px;color:var(--red);font-weight:500;font-size:13px;word-spacing:2px}
.footer-legal{left:780px;top:16px;list-style:none;line-height:16px}
.footer-legal li::before{content:"\25B8 ";font-size:8px}
</style>
</head>
<body>
<div class="page">
  <header class="header abs">
    <div class="brand abs"><span class="brand-dot"></span>Rent a Velvet</div>
    <div class="account abs">
      <svg width="22" height="22" viewBox="0 0 22 22"><circle cx="11" cy="7" r="5" fill="#666"/><path d="M1 21c0-6 4-8 10-8s10 2 10 8z" fill="#666"/></svg>
      <span>My Account</span><span class="sep">|</span><span>Login or Register</span>
    </div>
    <div class="social abs"><span></span><span></span></div>
    <form class="search abs"><input type="text" value="Search" aria-label="Search"><button type="button">GO</button></form>
  </header>

  <nav class="nav abs">
    <a class="active" href="#">HOME</a><a href="#">SEMPER</a><a href="#">NUSQUAM</a><a href="#">LEGERE</a><a href="#">ELECTRAM</a><a href="#">OMNIUS REBUS</a><a href="#">CONTACT</a>
  </nav>

  <section class="hero abs"></section>
  <h1 class="hero-title abs">PRINCIPES CAUSAE</h1>
  <div class="hero-sub abs">SUMA</div>
  <p class="hero-text abs">Solet iuvaret iudicabit nec ea, ne has enim propriae. Ex nec mazim imperdiet, decore nullam repudiandae ut ius. Elitr tation quo et,</p>
  <a class="btn hero-btn abs" href="#">READ MORE
    <svg width="34" height="34" viewBox="0 0 34 34"><circle cx="17" cy="17" r="16" fill="#fff"/><path d="M8 15h11v-6l8 8-8 8v-6H8z" fill="#111"/></svg></a>
  <div class="model abs" role="img" aria-label="Full-length photo of a model in black lace lingerie"></div>
  <div class="dots abs"><span></span><span class="on"></span><span></span><span></span></div>

  <div class="rule abs" style="top:605px"></div>

  <article class="card abs" style="left:40px">
    <div class="card-photo abs" role="img" aria-label="Model portfolio photo"></div>
    <h3 class="card-title abs">SOLET IUVARET IUDICABIT<br>NEC EA NE HAS ENIM</h3>
    <p class="card-note abs">SOLET IUVARET IUDICABIT NEC</p>
  </article>
  <article class="card abs" style="left:250px">
    <div class="card-photo abs" role="img" aria-label="Model portfolio photo"></div>
    <h3 class="card-title abs">SOLET IUVARET IUDICABIT<br>NEC EA NE HAS ENIM</h3>
    <p class="card-note abs">SOLET IUVARET IUDICABIT NEC</p>
  </article>
  <article class="card abs" style="left:460px">
    <div class="card-photo abs" role="img" aria-label="Model portfolio photo"></div>
    <h3 class="card-title abs">SOLET IUVARET IUDICABIT<br>NEC EA NE HAS ENIM</h3>
    <p class="card-note abs">SOLET IUVARET IUDICABIT NEC</p>
  </article>

  <h2 class="section-title services abs">Solet iuvaret iudicabit</h2>
  <ul class="service-list abs">
    <li>Reformidans</li><li>Reformidans</li>
    <li>Iuvaret</li><li>Iuvaret</li>
    <li>Consequuntur</li><li>Consequuntur</li>
    <li>Ullamcorper</li><li>Ullamcorper</li>
    <li>Essent</li><li>Essent</li>
    <li>Gloriatur</li><li>Gloriatur</li>
    <li>Dicam</li><li>Dicam</li>
    <li>Primis</li><li>Primis</li>
    <li>Scriptorem</li><li>Scriptorem</li>
    <li>Nulla</li><li>Nulla</li>
    <li>Dolore</li><li>Dolore</li>
    <li>Aliquando</li><li>Aliquando</li>
  </ul>

  <div class="rule abs" style="top:1031px"></div>

  <article class="post abs" style="left:40px">
    <h2 class="section-title abs" style="left:1px;top:0">Solet iuvaret iudicabit</h2>
    <div class="post-photo abs" role="img" aria-label="Model photo for blog post"></div>
    <h3 class="post-head abs">Solet iuvaret iudicabit nec</h3>
    <p class="post-text abs">Solet iuvaret iudicabit nec ea, ne has enim propriae. Ex nec mazim imperdiet, decore nullam repudiandae ut ius. Elitr tation quo et, no cum odio agam munere. No cum</p>
    <a class="btn post-btn abs" href="#">READ MORE
      <svg width="17" height="17" viewBox="0 0 34 34"><circle cx="17" cy="17" r="16" fill="#fff"/><path d="M8 15h11v-6l8 8-8 8v-6H8z" fill="#111"/></svg></a>
  </article>
  <article class="post abs" style="left:521px">
    <h2 class="section-title abs" style="left:1px;top:0">Solet iuvaret iudicabit</h2>
    <div class="post-photo abs" role="img" aria-label="Model photo for blog post"></div>
    <h3 class="post-head abs">Solet iuvaret iudicabit nec</h3>
    <p class="post-text abs">Solet iuvaret iudicabit nec ea, ne has enim propriae. Ex nec mazim imperdiet, decore nullam repudiandae ut ius. Elitr tation quo et, no cum odio agam munere. No cum</p>
    <a class="btn post-btn abs" href="#">READ MORE
      <svg width="17" height="17" viewBox="0 0 34 34"><circle cx="17" cy="17" r="16" fill="#fff"/><path d="M8 15h11v-6l8 8-8 8v-6H8z" fill="#111"/></svg></a>
  </article>

  <div class="rule abs" style="top:1237px"></div>

  <footer class="footer abs">
    <p class="footer-text abs">Usu vide iudicabit ex. Libris voluptua vix in, falli nobis necessitatibus per ut. An sit vidit invidunt definiebas, eum quas tacimates assueverit ex. Ut magna velit iracundia mea, ei reque homero principes duo.</p>
    <p class="footer-links abs">Libris &nbsp;|&nbsp; Legimus &nbsp;|&nbsp; Efficiantur &nbsp;|&nbsp; Feugiat &nbsp;|&nbsp; Tractatos &nbsp;€&nbsp; Corpora &nbsp;|&nbsp; Forensibus &nbsp;|&nbsp; Propriae</p>
    <ul class="footer-legal abs"><li>Terms and Conditions</li><li>Privacy Policy</li></ul>
  </footer>
</div>
</body>
</html>
```